Bramwell Resources Ltd. - Refreshed business card challenge

A revised, refreshed business card design for my oil and gas company using my existing logo. Feel free to be as creative as you like!

Target Market(s)

bankers, lawyers

Industry/Entity Type

Oil And Gas Exploration

Contact Information for Business Card

See the "Must Haves" section

Font styles to use
Serif
Sans Serif

Colors

Designer to choose colors to be used in the design.

Requirements
Must have
• Existing business logo, name, title, email, phone number, business address
• Neil Hadley, CA, CPA
• Vice President Finance & Chief Financial Officer
• nhadley@bramwellresources-mail.com
• office: (587)555-0142
• cell: (403)555-0187
• 1400, 815 4 Street S.W.
• Calgary, AB
• T2P 4K8
Should not have
• Should not be plain and boring.

```html
<!DOCTYPE html>
<html lang="en">
<head>
<meta charset="utf-8">
<title>Neil Hadley – Bramwell Resources Ltd.</title>
<link rel="stylesheet" href="https://fonts.googleapis.com/css2?family=Bebas+Neue&display=swap">
<style>
  :root {
    --bg-deep: #16272a;
    --bg-mid: #2c4a4d;
    --bg-glow: #5f8486;
    --ink-white: #ffffff;
    --ink-green: #1f4a2b;
    --rule-light: #a9d3d6;
    --brand-green: #1f5a2f;
  }
  html, body {
    margin: 0;
    padding: 0;
    width: 1200px;
    height: 686px;
    overflow: hidden;
    background: var(--bg-deep);
  }
  .card {
    position: relative;
    width: 1200px;
    height: 686px;
    overflow: hidden;
    background:
      radial-gradient(ellipse 520px 380px at 470px 390px, rgba(95,132,134,0.75), rgba(95,132,134,0) 70%),
      radial-gradient(ellipse 900px 600px at 560px 330px, var(--bg-mid), var(--bg-deep) 85%);
    font-family: "Bebas Neue", "Oswald", sans-serif;
  }
  .name-first {
    position: absolute;
    left: 94px;
    top: 86px;
    margin: 0;
    font-size: 222px;
    line-height: 1;
    letter-spacing: 6px;
    color: var(--ink-white);
    font-weight: 400;
  }
  .name-last {
    position: absolute;
    left: 97px;
    top: 280px;
    margin: 0;
    font-size: 116px;
    line-height: 1;
    letter-spacing: 6px;
    color: var(--ink-green);
    -webkit-text-stroke: 2px var(--ink-white);
    font-weight: 400;
  }
  .accent-rule {
    position: absolute;
    left: 490px;
    top: 200px;
    width: 710px;
    height: 3px;
    background: linear-gradient(to right, rgba(169,211,214,0), var(--rule-light) 25%, var(--rule-light));
    opacity: 0.85;
  }
  .brand {
    position: absolute;
    right: 82px;
    bottom: 100px;
    display: flex;
    align-items: center;
    gap: 12px;
  }
  .brand-dot {
    width: 26px;
    height: 26px;
    border-radius: 50%;
    background: var(--brand-green);
  }
  .brand-name {
    font-size: 64px;
    line-height: 1;
    letter-spacing: 2px;
    color: var(--brand-green);
  }
</style>
</head>
<body>
  <div class="card">
    <h1 class="name-first">Neil</h1>
    <h2 class="name-last">Hadley</h2>
    <div class="accent-rule"></div>
    <div class="brand">
      <span class="brand-dot"></span>
      <span class="brand-name">Bramwell</span>
    </div>
  </div>
</body>
</html>
```